" ELA NAO FOI ABERTA AINDA MAS SERA EM 20 DIAS. A VARTEMI - uma empresa especializada na prestação de serviços terceirizados integrados, auxiliando nossos clientes a reduzir custos indiretos, focar em seu negócio principal, sem se preocupar com serviços de apoio, como limpeza, copa, portaria, segurança, administrativo, zeladoria, telefonia e recepção. Uma empresa ou Condomínio apresenta necessidades diversas para se manter operando de maneira lucrativa e segura. Antes, cada negócio precisava atender às demandas por meio de sua infraestrutura interna. Mas uma opção vantajosa vem crescendo no mercado e merece destaque atualmente: a terceirização de atividades "

```html
<!DOCTYPE html>
<html lang="pt-BR">
<head>
<meta charset="UTF-8">
<title>Vartemi – Crachá funcional</title>
<link href="https://fonts.googleapis.com/css2?family=Montserrat:ital,wght@0,400;0,500;0,600;0,700;1,700;1,800&display=swap" rel="stylesheet">
<style>
  :root {
    --page-bg: #eceef0;
    --card-white: #ffffff;
    --card-shade: #e9ecef;
    --field-band: #e4e6e9;
    --field-border: #b9bdc2;
    --ink: #1c1f24;
    --ink-soft: #4a4f57;
    --brand-gold: #c9a718;
    --brand-navy: #1f3f7a;
    --accent-blue: #3a6fb8;
    --strip-yellow: #f2c200;
  }
  * { box-sizing: border-box; margin: 0; padding: 0; }
  html, body {
    width: 1200px; height: 1200px; overflow: hidden;
    background: var(--page-bg);
    font-family: "Montserrat", sans-serif;
    color: var(--ink);
  }
  .canvas {
    width: 1200px; height: 1200px;
    display: flex; align-items: center; justify-content: center;
  }
  .badge {
    position: relative;
    width: 640px; height: 900px;
    border-radius: 22px;
    background: linear-gradient(160deg, var(--card-white) 55%, var(--card-shade) 100%);
    box-shadow: 0 18px 40px rgba(0,0,0,0.14);
    overflow: hidden;
  }
  .badge__slot {
    position: absolute; top: 30px; left: 50%;
    width: 120px; height: 18px; margin-left: -60px;
    border-radius: 9px; background: var(--page-bg);
    box-shadow: inset 0 2px 3px rgba(0,0,0,0.15);
  }
  .badge__wave { position: absolute; left: 0; top: 0; width: 640px; height: 900px; }
  .brand {
    position: absolute; top: 80px; left: 0; right: 0;
    display: flex; align-items: center; justify-content: center; gap: 14px;
  }
  .brand__dot { width: 44px; height: 44px; border-radius: 50%; background: var(--brand-navy); }
  .brand__name {
    font-weight: 700; font-size: 46px; letter-spacing: 4px; color: var(--brand-gold);
  }
  .fields {
    position: absolute; top: 190px; left: 70px; right: 40px;
    display: flex; flex-direction: column; gap: 16px;
  }
  .field {
    background: var(--field-band);
    padding: 8px 14px 10px;
    border-radius: 4px;
  }
  .field__label { font-size: 20px; font-weight: 500; color: var(--ink-soft); margin-bottom: 4px; }
  .field__value {
    background: var(--card-white);
    border: 1.5px solid var(--field-border);
    padding: 6px 12px;
    font-size: 24px; font-weight: 800; font-style: italic; letter-spacing: 0.5px;
  }
  .notice {
    position: absolute; top: 700px; left: 150px; right: 40px;
    text-align: center; font-size: 19px; font-weight: 700; font-style: italic; line-height: 1.35;
  }
  .contacts {
    position: absolute; top: 780px; left: 60px;
    display: flex; flex-direction: column; gap: 6px;
    font-size: 12px; color: var(--ink-soft);
  }
  .contact { display: flex; align-items: flex-start; gap: 8px; line-height: 1.3; }
  .contact__icon { width: 16px; height: 16px; flex: none; }
  .signature-box {
    position: absolute; right: 70px; bottom: 40px;
    width: 190px; height: 56px;
    background: var(--card-white); border: 1.5px solid var(--field-border);
  }
  .badge__strip {
    position: absolute; left: 0; right: 0; bottom: 0; height: 14px;
    background: var(--strip-yellow);
  }
</style>
</head>
<body>
<main class="canvas">
  <section class="badge" aria-label="Crachá funcional Vartemi">
    <svg class="badge__wave" viewBox="0 0 640 900" aria-hidden="true">
      <path d="M0 0 H55 C30 300 30 600 55 900 H0 Z" fill="#dfe3e8"/>
      <path d="M0 740 C200 700 400 760 640 720 V900 H0 Z" fill="#f1f3f5"/>
    </svg>
    <div class="badge__slot"></div>

    <header class="brand">
      <span class="brand__dot"></span>
      <span class="brand__name">VARTEMI</span>
    </header>

    <div class="fields">
      <div class="field">
        <p class="field__label">Nome do funcionário</p>
        <p class="field__value">MARIANA COSTA</p>
      </div>
      <div class="field">
        <p class="field__label">Data Admissão</p>
        <p class="field__value">00/00/0000</p>
      </div>
      <div class="field">
        <p class="field__label">RG</p>
        <p class="field__value">0000000000-00</p>
      </div>
      <div class="field">
        <p class="field__label">Matrícula</p>
        <p class="field__value">0000-00</p>
      </div>
    </div>

    <p class="notice">É obrigatório o porte desta identidade<br>funcional em local visível.</p>

    <div class="contacts">
      <div class="contact">
        <svg class="contact__icon" viewBox="0 0 16 16" aria-hidden="true"><circle cx="8" cy="8" r="7" fill="var(--accent-blue)"/><circle cx="8" cy="8" r="3" fill="none" stroke="#fff" stroke-width="1.5"/></svg>
        <span>@vartemi</span>
      </div>
      <div class="contact">
        <svg class="contact__icon" viewBox="0 0 16 16" aria-hidden="true"><circle cx="8" cy="8" r="7" fill="var(--accent-blue)"/><path d="M8 3.5a3 3 0 0 0-3 3c0 2.3 3 5.5 3 5.5s3-3.2 3-5.5a3 3 0 0 0-3-3z" fill="#fff"/><circle cx="8" cy="6.5" r="1" fill="var(--accent-blue)"/></svg>
        <span>Rua das Palmeiras, 480 - Centro<br>Jardim Aurora - RJ<br>CEP 24000-000</span>
      </div>
      <div class="contact">
        <svg class="contact__icon" viewBox="0 0 16 16" aria-hidden="true"><circle cx="8" cy="8" r="7" fill="var(--accent-blue)"/><rect x="4" y="5" width="8" height="6" fill="none" stroke="#fff" stroke-width="1.2"/><path d="M4 5l4 3.5L12 5" fill="none" stroke="#fff" stroke-width="1.2"/></svg>
        <span>contato@vartemi.com</span>
      </div>
    </div>

    <div class="signature-box" aria-label="Campo para assinatura"></div>
    <div class="badge__strip"></div>
  </section>
</main>
</body>
</html>
```